Accounting firm needing business card / letterhead designed
Marcus L. Tembrook, CPA
marcus@lumenfiledesk.com
www.lumenfiledesk.com
482 E Larkin Ave Perrysburg, OH 43566
419-555-0172
Business

```html
<!DOCTYPE html>
<html lang="en">
<head>
<meta charset="utf-8">
<title>Lumen File Desk – Business Card</title>
<link rel="stylesheet" href="https://fonts.googleapis.com/css2?family=Barlow+Semi+Condensed:wght@500;600&family=Barlow:wght@600&display=swap">
<style>
  :root {
    --page-bg: #e4e4e4;
    --card-front: #2e2f30;
    --card-back: #22144a;
    --accent-green: #6cbf2a;
    --text-light: #f2f2f2;
    --text-soft: #e6e6e6;
  }
  * { box-sizing: border-box; margin: 0; padding: 0; }
  html, body {
    width: 1200px; height: 576px; overflow: hidden;
    background: var(--page-bg);
  }
  .canvas { position: relative; width: 1200px; height: 576px; }
  .card {
    position: absolute; top: 139px;
    width: 484px; height: 292px;
    border-radius: 14px;
    box-shadow: 0 3px 6px rgba(0,0,0,0.25);
    overflow: hidden;
  }
  .card--front { left: 82px; background: var(--card-front); }
  .card--back { left: 602px; background: var(--card-back); }

  .holder-name {
    position: absolute; left: 29px; top: 48px;
    font-family: "Barlow Semi Condensed", sans-serif;
    font-weight: 600; font-size: 19px;
    color: var(--text-light);
  }
  .holder-name .credential { color: var(--accent-green); }

  .contact-list {
    position: absolute; left: 29px; top: 85px;
    list-style: none;
    font-family: "Barlow Semi Condensed", sans-serif;
    font-weight: 500; font-size: 12.5px;
    color: var(--text-soft);
  }
  .contact-item {
    display: flex; align-items: center;
    height: 15.5px;
  }
  .contact-icon {
    width: 11px; height: 11px; margin-right: 13px;
    fill: var(--accent-green);
  }
  .address {
    position: absolute; left: 29px; top: 186px;
    font-family: "Barlow Semi Condensed", sans-serif;
    font-weight: 500; font-size: 12.5px;
    color: var(--text-soft);
  }

  .brand-name {
    position: absolute;
    font-family: "Barlow", sans-serif;
    font-weight: 600; font-size: 30px;
    letter-spacing: 1px; text-transform: uppercase;
    color: var(--text-light);
    white-space: nowrap;
  }
  .card--front .brand-name { left: 29px; bottom: 36px; }
  .card--back .brand-name { right: 30px; bottom: 38px; }
</style>
</head>
<body>
<main class="canvas">
  <section class="card card--front" aria-label="Business card front">
    <h1 class="holder-name">Marcus L. Tembrook, <span class="credential">CPA</span></h1>
    <ul class="contact-list">
      <li class="contact-item">
        <svg class="contact-icon" viewBox="0 0 12 12" aria-hidden="true"><path d="M1 4c0-2 2-3 5-3s5 1 5 3v1H8.5V3.8H3.5V5H1z"/><rect x="2.5" y="6" width="7" height="5" rx="1"/></svg>
        419-555-0172
      </li>
      <li class="contact-item">
        <svg class="contact-icon" viewBox="0 0 12 12" aria-hidden="true"><path d="M0.5 2.5h11v7h-11z M1.5 3.3l4.5 3.5 4.5-3.5" fill="none" stroke="#6cbf2a" stroke-width="1.2"/><path d="M0.5 2.5h11l-5.5 4.3z"/></svg>
        marcus@lumenfiledesk.com
      </li>
      <li class="contact-item">
        <svg class="contact-icon" viewBox="0 0 12 12" aria-hidden="true"><circle cx="6" cy="6" r="5" fill="none" stroke="#6cbf2a" stroke-width="1.1"/><ellipse cx="6" cy="6" rx="2.2" ry="5" fill="none" stroke="#6cbf2a" stroke-width="1"/><path d="M1 6h10M2 3.5h8M2 8.5h8" stroke="#6cbf2a" stroke-width="0.9"/></svg>
        www.lumenfiledesk.com
      </li>
    </ul>
    <p class="address">482 E Larkin Ave Perrysburg, OH 43566</p>
    <p class="brand-name">Lumen File Desk</p>
  </section>

  <section class="card card--back" aria-label="Business card back">
    <p class="brand-name">Lumen File Desk</p>
  </section>
</main>
</body>
</html>
```